Brava Nest (Smart Home, Installation, Repair Industry) (Contest)

Looking for a website design for my company
Services we offer:
Phone Repair
TV Mounting
Security Camera Installation
Networking / Wi-Fi
Smart Home Services
IT Support

Looking for a website similar to trovely.example

Few tabs
About Us
Contact Us
Areas Served
Pricing and Services

```html
<!DOCTYPE html>
<html lang="en">
<head>
<meta charset="utf-8">
<title>Brava Nest – Home Maintenance Made Simple</title>
<link href="https://fonts.googleapis.com/css2?family=Poppins:ital,wght@0,400;0,500;0,600;0,700;1,600;1,700&family=Open+Sans:wght@400;600&display=swap" rel="stylesheet">
<style>
:root{
  --orange:#f7941d;
  --orange-dark:#e8830b;
  --grey:#7d7d7d;
  --grey-dark:#5e5e5e;
  --ink:#2a2a2a;
  --text:#555;
  --card:#f2f2f2;
  --footer:#2b2b2b;
  --white:#fff;
}
*{margin:0;padding:0;box-sizing:border-box}
html,body{width:1200px;height:4713px;overflow:hidden}
body{position:relative;background:var(--white);font-family:"Open Sans",Arial,sans-serif;color:var(--text);font-size:12px}
.abs{position:absolute}
h1,h2,h3,h4,.brand,.nav a,.btn{font-family:"Poppins",Arial,sans-serif}
.brand{font-weight:700;font-size:44px;color:var(--orange);letter-spacing:-.5px;line-height:1}
.brand--light{color:var(--orange)}

/* header */
.site-header{top:0;left:0;width:1200px;height:115px;background:var(--white)}
.site-header .brand{left:68px;top:40px}
.contact-chip{top:26px;display:flex;align-items:center;gap:9px;font-size:11px;color:#555;line-height:1.3}
.contact-chip .ic{width:24px;height:24px;border-radius:50%;background:#fde9d2;display:flex;align-items:center;justify-content:center}
.contact-chip small{color:var(--orange);display:block;font-size:10px}
.nav{top:72px;left:551px;display:flex;gap:0}
.nav a{font-size:13px;color:#555;text-decoration:none;margin-right:43px;position:relative}
.nav a.active{color:var(--orange)}
.nav a.active::after{content:"";position:absolute;left:6px;right:6px;bottom:-10px;height:2px;background:var(--orange)}

.btn{display:inline-flex;align-items:center;height:34px;border-radius:17px;background:var(--orange);color:#fff;font-size:12px;text-decoration:none;overflow:hidden}
.btn span{padding:0 20px}
.btn .tool{width:42px;height:100%;background:var(--grey);display:flex;align-items:center;justify-content:center;border-radius:0 17px 17px 0}
.btn--plain{justify-content:center;padding:0 28px}
.btn--grey{background:var(--grey);justify-content:center}

/* hero */
.hero{top:115px;left:0;width:1200px;height:570px;overflow:hidden}
.hero .photo{width:100%;height:100%;background:linear-gradient(90deg,#6f6a66 0%,#b9b3ad 35%,#d7d1ca 65%,#c7bfb6 100%)}
.hero h1{top:225px;width:1200px;text-align:center;color:#fff;font-style:italic;font-weight:700;font-size:31px;line-height:1.25;text-shadow:0 2px 6px rgba(0,0,0,.25)}
.hero .btn{top:317px;left:510px}
.hero svg{bottom:0;left:0}
.slider-dots{top:697px;left:576px;display:flex;gap:7px}
.slider-dots i{width:5px;height:5px;border-radius:50%;background:#999;display:block}
.slider-dots i.on{background:var(--orange)}

/* section titles */
.section-title{width:1200px;text-align:center;font-family:"Poppins",sans-serif;font-weight:500;color:var(--ink);font-size:29px}

/* services */
.services-title{top:745px}
.services-deco{top:797px;left:570px}
.service{width:340px;height:242px;background:var(--card);text-align:center;padding-top:32px}
.service svg{display:block;margin:0 auto 12px}
.service h3{font-size:16px;font-weight:500;color:var(--ink);margin-bottom:12px}
.service p{font-size:11px;line-height:1.4;width:240px;margin:0 auto;color:#555}
.service--active{background:var(--orange)}
.service--active h3,.service--active p{color:#fff}

/* feature band */
.feature{top:1481px;left:0;width:1200px;height:522px;background:linear-gradient(90deg,#e9ecef 0%,#eef0f2 60%,#d9dde1 100%)}
.feature .photo{right:0;top:0;width:400px;height:522px;background:linear-gradient(135deg,#cfd3d6,#8a8f94)}
.feature h2{left:73px;top:152px;font-style:italic;font-weight:600;font-size:30px;color:var(--ink);line-height:1.25}
.feature p{left:73px;width:450px;font-size:11.5px;line-height:1.4;color:#555}
.feature .btn{left:73px;top:379px;height:32px}

/* pricing */
.pricing-title{top:2050px}
.pricing-sub{top:2098px;width:1200px;text-align:center;font-size:13px;color:#666}
.plan{background:#f4f4f4;box-shadow:0 0 0 1px #eaeaea;text-align:center}
.plan-head{background:var(--grey);color:#fff;position:relative}
.plan-head h3{font-weight:500;font-size:18px}
.plan-head .price{font-family:"Poppins",sans-serif;font-weight:600;font-size:30px}
.plan-head .price small{font-size:9px;font-weight:400}
.plan-badge{position:absolute;left:50%;bottom:-22px;margin-left:-22px;width:44px;height:44px;border-radius:50%;background:var(--orange);border:3px solid #fff;display:flex;align-items:center;justify-content:center}
.plan ul{list-style:none;text-align:left;font-size:12px;color:#555}
.plan li{display:flex;align-items:center;gap:10px;height:27px}
.plan .btn{height:34px}
.plan--featured .plan-head{background:var(--orange)}
.plan--featured .plan-badge{background:var(--grey)}
.carousel-arrow{width:30px;height:30px;border-radius:50%;border:2px solid;display:flex;align-items:center;justify-content:center}

/* testimonials */
.testimonials{top:2751px;left:0;width:1200px;height:519px;background:linear-gradient(90deg,#2a2623,#4a433d 50%,#2c2825);border-bottom:4px solid var(--orange);color:#fff;text-align:center}
.testimonials h2{top:98px;width:1200px;font-weight:600;font-size:29px}
.testimonials .sub{top:146px;width:1200px;font-size:13px}
.avatar{top:180px;left:555px;width:90px;height:90px;border-radius:50%;background:linear-gradient(#d8d2cc,#9c948c);border:3px solid #fff}
.testimonials .name{top:282px;width:1200px;font-family:"Poppins";font-size:16px}
.testimonials .role{top:303px;width:1200px;font-size:12px}
.testimonials .quote{top:334px;left:215px;width:770px;font-size:12.5px;line-height:1.35}
.q-mark{font-family:Georgia,serif;font-size:34px;font-weight:700}
.testimonials .slider-dots{top:422px;left:565px}
.testimonials .slider-dots i{background:#fff}
.testimonials .slider-dots i.on{background:var(--orange)}

/* blogs */
.blogs-title{top:3332px}
.post{width:327px;height:383px;background:var(--card);top:3404px}
.post .photo{height:192px}
.post .meta{display:flex;justify-content:space-between;padding:14px 16px 0;font-size:12px;color:#555}
.post h4{font-weight:400;font-size:14px;color:#444;padding:24px 16px 10px}
.post p{font-size:11.5px;line-height:1.35;padding:0 16px;color:#555}
.post a{display:inline-block;margin:14px 16px 0;font-size:13px;color:#555;letter-spacing:.5px}

/* about */
.about h2{left:148px;top:3946px;font-weight:500;font-size:30px;color:var(--ink)}
.about .rule{left:150px;top:4000px;width:60px;height:2px;background:var(--grey)}
.about p{left:148px;width:448px;font-size:11.5px;line-height:1.35;color:#555}
.about .btn{left:148px;top:4218px;height:34px}
.about .photo{left:655px;top:3920px;width:440px;height:390px;background:linear-gradient(160deg,#ffffff 0%,#f1ece3 50%,#e5dccd 100%)}

/* footer */
.footer-wave{top:4270px;left:0}
.site-footer{top:4340px;left:0;width:1200px;height:292px;background:var(--footer);color:#fff}
.site-footer .brand{left:73px;top:122px}
.foot-col h4{font-weight:500;font-size:13px;margin-bottom:26px}
.foot-col ul{list-style:none;font-size:12px;line-height:2.1}
.foot-col li::before{content:"•";margin-right:8px}
.info-row{display:flex;gap:12px;font-size:11.5px;line-height:1.6;align-items:flex-start}
.field{background:#3d3d3d;border:1px solid #4a4a4a;font-size:12px;color:#aaa;padding:6px 12px}
.copyright{top:4669px;left:73px;font-size:11px;color:#555}
.social{top:4652px;display:flex;gap:12px;left:940px}
.social i{display:block;width:34px;height:34px;border-radius:50%;background:var(--ink)}
.social i.first{background:var(--orange)}
</style>
</head>
<body>

<!-- Header -->
<header class="site-header abs">
  <div class="brand abs">Brava Nest</div>
  <div class="contact-chip abs" style="left:655px">
    <span class="ic"><svg width="12" height="12" viewBox="0 0 24 24"><path d="M6 2l4 4-2 3c1 3 4 6 7 7l3-2 4 4-3 4C10 21 3 14 3 5z" fill="#f7941d"/></svg></span>
    <div><small>Call Us</small>555-014-2290</div>
  </div>
  <div class="contact-chip abs" style="left:817px">
    <span class="ic"><svg width="12" height="10" viewBox="0 0 24 18"><rect x="1" y="1" width="22" height="16" rx="2" fill="none" stroke="#f7941d" stroke-width="2"/><path d="M1 2l11 8 11-8" fill="none" stroke="#f7941d" stroke-width="2"/></svg></span>
    <div><small>Email us</small>hello@bravanest.example</div>
  </div>
  <a class="btn abs" style="top:22px;left:984px;height:34px"><span style="padding:0 12px 0 18px">Book a Service</span><i class="tool"><svg width="16" height="14" viewBox="0 0 16 14"><path d="M2 7h8M10 3l4 4-4 4" fill="none" stroke="#fff" stroke-width="2"/></svg></i></a>
  <nav class="nav abs">
    <a class="active" href="#">Home</a>
    <a href="#">About Us</a>
    <a href="#">Areas Served</a>
    <a href="#">Pricing and Services</a>
    <a href="#" style="margin-right:0">Contact Us</a>
  </nav>
</header>

<!-- Hero -->
<section class="hero abs">
  <div class="photo" role="img" aria-label="Technician mounting a television while a smiling homeowner gives a thumbs up from the sofa"></div>
  <h1 class="abs">Home Maintenance<br>Made Simple</h1>
  <a class="btn abs"><span>Book A Service</span><i class="tool"><svg width="16" height="14" viewBox="0 0 16 14"><path d="M2 7h8M10 3l4 4-4 4" fill="none" stroke="#fff" stroke-width="2"/></svg></i></a>
  <svg class="abs" width="1200" height="130" viewBox="0 0 1200 130">
    <path d="M0 130 L0 110 Q500 10 1200 40 L1200 130Z" fill="#6f6f6f"/>
    <path d="M0 130 L0 80 Q250 115 520 70 Q700 45 1200 45 L1200 130Z" fill="#f7941d"/>
    <path d="M0 130 L0 100 Q300 130 600 85 Q850 55 1200 60 L1200 130Z" fill="#fff"/>
  </svg>
</section>
<div class="slider-dots abs"><i></i><i class="on"></i><i></i><i></i></div>

<!-- Services -->
<h2 class="section-title abs services-title">Services We Offer</h2>
<svg class="services-deco abs" width="60" height="16" viewBox="0 0 60 16"><path d="M6 8h48M2 3l6 5-6 5M58 3l-6 5 6 5" fill="none" stroke="#f7941d" stroke-width="3"/></svg>

<div class="service abs" style="left:73px;top:845px">
  <svg width="56" height="64" viewBox="0 0 56 64" fill="none" stroke="#333" stroke-width="2"><rect x="10" y="2" width="26" height="52" rx="3"/><line x1="18" y1="48" x2="28" y2="48"/><circle cx="34" cy="36" r="8" stroke="#f7941d"/><circle cx="34" cy="36" r="3" stroke="#f7941d"/></svg>
  <h3>Phone Repair</h3>
  <p>Lorem Ipsum is a simply dummy text has been the industry standard dummy text ever since the 1500s.</p>
</div>
<div class="service service--active abs" style="left:430px;top:845px">
  <svg width="90" height="64" viewBox="0 0 90 64" fill="none" stroke="#fff" stroke-width="2"><rect x="2" y="12" width="50" height="34"/><rect x="50" y="6" width="30" height="44"/><path d="M56 14h18M56 24h18M56 34h18M62 6v44M70 6v44"/></svg>
  <h3>TV Mounting</h3>
  <p>Lorem Ipsum is a simply dummy text has been the industry standard dummy text ever since the 1500s.</p>
</div>
<div class="service abs" style="left:785px;top:845px">
  <svg width="76" height="64" viewBox="0 0 76 64" fill="none" stroke="#333" stroke-width="2"><rect x="2" y="4" width="72" height="16"/><path d="M8 20q30 40 60 0"/><circle cx="38" cy="34" r="10"/><circle cx="38" cy="34" r="4" stroke="#f7941d"/></svg>
  <h3>Security Camera Installation</h3>
  <p>Lorem Ipsum is a simply dummy text has been the industry standard dummy text ever since the 1500s.</p>
</div>
<div class="service abs" style="left:73px;top:1099px">
  <svg width="80" height="64" viewBox="0 0 80 64" fill="none" stroke="#333" stroke-width="2"><rect x="6" y="36" width="68" height="18" rx="2"/><path d="M18 36V14M62 36V14M14 45h8M28 45h8" /><path d="M30 20q10-10 20 0M34 26q6-6 12 0" stroke="#f7941d"/></svg>
  <h3>Networking / Wi-Fi</h3>
  <p>Lorem Ipsum is a simply dummy text of has been the industry standard dummy text ever since the 1500s.</p>
</div>
<div class="service abs" style="left:430px;top:1099px">
  <svg width="64" height="64" viewBox="0 0 64 64" fill="none" stroke="#333" stroke-width="2"><path d="M8 28L32 6l24 22M16 22v34h32V22"/><path d="M24 56V38M32 56V30M40 56V38" stroke="#f7941d"/><circle cx="32" cy="26" r="3"/></svg>
  <h3>Smart Home Services</h3>
  <p>Lorem Ipsum is a simply dummy text of has been the industry standard dummy text ever since the 1500s.</p>
</div>
<div class="service abs" style="left:785px;top:1099px">
  <svg width="70" height="64" viewBox="0 0 70 64" fill="none" stroke="#333" stroke-width="2"><path d="M26 60V34l-10-10M44 60V34l10-10M26 34h18"/><circle cx="14" cy="14" r="6" stroke="#f7941d"/><circle cx="56" cy="14" r="6" stroke="#f7941d"/><path d="M30 20h10M35 14v12"/></svg>
  <h3>IT Support</h3>
  <p>Lorem Ipsum is a simply dummy text of has been the industry standard dummy text ever since the 1500s.</p>
</div>
<a class="btn abs" style="left:508px;top:1390px;height:32px"><span style="padding:0 22px 0 40px">View More</span><i class="tool" style="width:42px"><svg width="16" height="14" viewBox="0 0 16 14"><path d="M2 7h8M10 3l4 4-4 4" fill="none" stroke="#fff" stroke-width="2"/></svg></i></a>

<!-- Feature band -->
<section class="feature abs">
  <div class="photo abs" style="left:460px;width:740px;background:linear-gradient(90deg,rgba(233,236,239,0),#c9cdd1 30%,#8f7f77 70%,#6c5a52)" role="img" aria-label="Hands installing a white security camera on a wall with a cordless drill"></div>
  <h2 class="abs">Security Camera<br>Installation</h2>
  <p class="abs" style="top:250px">Lorem Ipsum is simply dummy text of the printing and typesetting industry has been the industry's standard dummy text ever since the 1500s,</p>
  <p class="abs" style="top:310px">when an unknown printer took a galley of type and scrambled it to make a into electronic typesetting, remaining essentially unchanged. It was popularised in the 1960s</p>
  <a class="btn btn--plain abs"><span style="padding:0 10px">Read More</span></a>
</section>

<!-- Pricing -->
<h2 class="section-title abs pricing-title">Pricing</h2>
<div class="pricing-sub abs">Choose Your Plan</div>

<div class="carousel-arrow abs" style="left:75px;top:2378px;border-color:#bbb"><svg width="10" height="12" viewBox="0 0 10 12"><path d="M8 1L2 6l6 5" fill="none" stroke="#bbb" stroke-width="2"/></svg></div>
<div class="carousel-arrow abs" style="left:1092px;top:2378px;border-color:var(--orange)"><svg width="10" height="12" viewBox="0 0 10 12"><path d="M2 1l6 5-6 5" fill="none" stroke="#f7941d" stroke-width="2"/></svg></div>

<div class="plan abs" style="left:132px;top:2175px;width:270px;height:424px">
  <div class="plan-head" style="height:160px;padding-top:22px">
    <svg width="30" height="36" viewBox="0 0 30 36" fill="none" stroke="#fff" stroke-width="2"><rect x="4" y="2" width="16" height="30" rx="2"/><circle cx="20" cy="22" r="5"/></svg>
    <h3>Phone Repair</h3>
    <div class="price">$00.00 <small>/Year</small></div>
    <span class="plan-badge"><svg width="16" height="14" viewBox="0 0 16 14"><path d="M2 7h8M10 3l4 4-4 4" fill="none" stroke="#fff" stroke-width="2"/></svg></span>
  </div>
  <ul style="padding:36px 0 0 26px">
    <li><svg width="14" height="14"><circle cx="7" cy="7" r="6" fill="none" stroke="#999"/><path d="M4 7l2 2 4-4" fill="none" stroke="#999"/></svg>Lorem Ipsum is simply dummy.</li>
    <li><svg width="14" height="14"><circle cx="7" cy="7" r="6" fill="none" stroke="#999"/><path d="M4 7l2 2 4-4" fill="none" stroke="#999"/></svg>The printing and typesetting</li>
    <li><svg width="14" height="14"><circle cx="7" cy="7" r="6" fill="none" stroke="#999"/><path d="M4 7l2 2 4-4" fill="none" stroke="#999"/></svg>Industry has been the industry.</li>
    <li><svg width="14" height="14"><circle cx="7" cy="7" r="6" fill="none" stroke="#999"/><path d="M4 7l2 2 4-4" fill="none" stroke="#999"/></svg>Standard dummy text ever since</li>
    <li><svg width="14" height="14"><circle cx="7" cy="7" r="6" fill="none" stroke="#999"/><path d="M4 7l2 2 4-4" fill="none" stroke="#999"/></svg>100% satisfaction</li>
  </ul>
  <a class="btn btn--grey" style="width:162px;margin-top:24px">BOOK NOW</a>
</div>

<div class="plan plan--featured abs" style="left:430px;top:2145px;width:340px;height:507px">
  <div class="plan-head" style="height:190px;padding-top:20px">
    <svg width="56" height="44" viewBox="0 0 80 64" fill="none" stroke="#fff" stroke-width="3"><rect x="6" y="36" width="68" height="18" rx="2"/><path d="M18 36V14M62 36V14M30 20q10-10 20 0M34 26q6-6 12 0"/></svg>
    <h3 style="font-size:21px">Networking / Wi-Fi</h3>
    <div class="price" style="font-size:34px">$00.00 <small>/Year</small></div>
    <span class="plan-badge" style="width:50px;height:50px;margin-left:-25px;bottom:-25px"><svg width="16" height="14" viewBox="0 0 16 14"><path d="M2 7h8M10 3l4 4-4 4" fill="none" stroke="#fff" stroke-width="2"/></svg></span>
  </div>
  <ul style="padding:36px 0 0 44px">
    <li><svg width="14" height="14"><circle cx="7" cy="7" r="6" fill="none" stroke="#999"/><path d="M4 7l2 2 4-4" fill="none" stroke="#999"/></svg>Lorem Ipsum is simply dummy.</li>
    <li><svg width="14" height="14"><circle cx="7" cy="7" r="6" fill="none" stroke="#999"/><path d="M4 7l2 2 4-4" fill="none" stroke="#999"/></svg>The printing and typesetting</li>
    <li><svg width="14" height="14"><circle cx="7" cy="7" r="6" fill="none" stroke="#999"/><path d="M4 7l2 2 4-4" fill="none" stroke="#999"/></svg>Industry has been the industry's</li>
    <li><svg width="14" height="14"><circle cx="7" cy="7" r="6" fill="none" stroke="#999"/><path d="M4 7l2 2 4-4" fill="none" stroke="#999"/></svg>Standard dummy text ever since</li>
    <li><svg width="14" height="14"><circle cx="7" cy="7" r="6" fill="none" stroke="#999"/><path d="M4 7l2 2 4-4" fill="none" stroke="#999"/></svg>When an unknown printer too</li>
    <li><svg width="14" height="14"><circle cx="7" cy="7" r="6" fill="none" stroke="#999"/><path d="M4 7l2 2 4-4" fill="none" stroke="#999"/></svg>Industry has been the industry's</li>
    <li><svg width="14" height="14"><circle cx="7" cy="7" r="6" fill="none" stroke="#999"/><path d="M4 7l2 2 4-4" fill="none" stroke="#999"/></svg>100% satisfaction</li>
  </ul>
  <a class="btn btn--plain" style="width:166px;margin-top:24px">ADD TO CART</a>
</div>

<div class="plan abs" style="left:794px;top:2175px;width:270px;height:424px">
  <div class="plan-head" style="height:160px;padding-top:22px">
    <svg width="34" height="36" viewBox="0 0 64 64" fill="none" stroke="#fff" stroke-width="3"><path d="M8 28L32 6l24 22M16 22v34h32V22M24 56V38M32 56V30M40 56V38"/></svg>
    <h3>Smart Home Services</h3>
    <div class="price">$00.00 <small>/Year</small></div>
    <span class="plan-badge"><svg width="16" height="14" viewBox="0 0 16 14"><path d="M2 7h8M10 3l4 4-4 4" fill="none" stroke="#fff" stroke-width="2"/></svg></span>
  </div>
  <ul style="padding:36px 0 0 26px">
    <li><svg width="14" height="14"><circle cx="7" cy="7" r="6" fill="none" stroke="#999"/><path d="M4 7l2 2 4-4" fill="none" stroke="#999"/></svg>Lorem Ipsum is simply dummy.</li>
    <li><svg width="14" height="14"><circle cx="7" cy="7" r="6" fill="none" stroke="#999"/><path d="M4 7l2 2 4-4" fill="none" stroke="#999"/></svg>The printing and typesetting</li>
    <li><svg width="14" height="14"><circle cx="7" cy="7" r="6" fill="none" stroke="#999"/><path d="M4 7l2 2 4-4" fill="none" stroke="#999"/></svg>Industry has been the industry.</li>
    <li><svg width="14" height="14"><circle cx="7" cy="7" r="6" fill="none" stroke="#999"/><path d="M4 7l2 2 4-4" fill="none" stroke="#999"/></svg>Standard dummy text ever since</li>
    <li><svg width="14" height="14"><circle cx="7" cy="7" r="6" fill="none" stroke="#999"/><path d="M4 7l2 2 4-4" fill="none" stroke="#999"/></svg>100% satisfaction</li>
  </ul>
  <a class="btn btn--grey" style="width:162px;margin-top:24px">BOOK NOW</a>
</div>

<!-- Testimonials -->
<section class="testimonials abs" role="img" aria-label="Dimmed living room scene behind client testimonials">
  <h2 class="abs">What client say about us</h2>
  <div class="sub abs">Testimonials</div>
  <div class="avatar abs" role="img" aria-label="Client portrait"></div>
  <div class="name abs">Daniel Marsh</div>
  <div class="role abs">Creative Director</div>
  <span class="q-mark abs" style="left:220px;top:292px">“</span>
  <p class="quote abs">Lorem Ipsum is simply dummy text of the printing and typesetting when an unknown printer took a galley of type Lorem Ipsum is simply dummy text of the printing and typesetting industry has been the industry's standard dummy into electronic typesetting, remaining essentially unchanged. It was popularised in the 1960</p>
  <span class="q-mark abs" style="left:878px;top:372px">”</span>
  <div class="slider-dots abs"><i></i><i class="on"></i><i></i><i></i><i></i></div>
</section>

<!-- Blogs -->
<h2 class="section-title abs blogs-title">Our Blogs</h2>
<article class="post abs" style="left:73px">
  <div class="photo" style="background:linear-gradient(135deg,#6b5443,#c9a98a)" role="img" aria-label="Bedroom with smart home control overlay"></div>
  <div class="meta"><span>▦ July 31, 2020</span><span>◯ 20 &nbsp; ♡ 12</span></div>
  <h4>Blog Title Heading</h4>
  <p>Lorem Ipsum is simply dummy text of the printing and typesetting industry has been the industry's standard dummy text ever since the 1500s.</p>
  <a>Read More</a>
</article>
<article class="post abs" style="left:435px">
  <div class="photo" style="background:linear-gradient(160deg,#9aa3ab,#e8e3da 55%,#c19a66)" role="img" aria-label="White Wi-Fi router on a wooden desk"></div>
  <div class="meta"><span>▦ July 31, 2020</span><span>◯ 20 &nbsp; ♡ 12</span></div>
  <h4>Blog Title Heading</h4>
  <p>Lorem Ipsum is simply dummy text of the printing and typesetting industry has been the industry's standard dummy text ever since the 1500s.</p>
  <a>Read More</a>
</article>
<article class="post abs" style="left:797px">
  <div class="photo" style="background:linear-gradient(135deg,#dde3e8,#7d8c99)" role="img" aria-label="IT support team working at a computer"></div>
  <div class="meta"><span>▦ July 31, 2020</span><span>◯ 20 &nbsp; ♡ 12</span></div>
  <h4>Blog Title Heading</h4>
  <p>Lorem Ipsum is simply dummy text of the printing and typesetting industry has been the industry's standard dummy text ever since the 1500s.</p>
  <a>Read More</a>
</article>
<a class="btn btn--plain abs" style="left:515px;top:3812px;width:165px;height:32px">VIEW MORE</a>

<!-- About -->
<section class="about">
  <h2 class="abs">About us</h2>
  <div class="rule abs"></div>
  <p class="abs" style="top:4020px">Lorem Ipsum is simply dummy text of the printing and typesetting industry has been the industry's standard dummy text ever since the 1500s,</p>
  <p class="abs" style="top:4066px">when an unknown printer took a galley of type and scrambled it to make a type specimen book. It has survived not only five centuries, but also the leap into electronic typesetting, remaining essentially unchanged. It was popularised in the 1960s</p>
  <p class="abs" style="top:4148px">with the release of Lettrine sheets containing Lorem Ipsum passages, and more recently with desktop publishing software like Pagewright Desktop including versions of Lorem Ipsum.</p>
  <a class="btn btn--plain abs" style="width:165px">Read More</a>
  <div class="photo abs" role="img" aria-label="Handyman in a hard hat holding several tools"></div>
</section>

<!-- Footer -->
<svg class="footer-wave abs" width="1200" height="80" viewBox="0 0 1200 80">
  <path d="M0 80 L0 40 Q400 75 700 30 Q950 0 1200 10 L1200 80Z" fill="#7a7a7a"/>
  <path d="M0 80 L0 50 Q300 30 620 45 Q900 55 1200 25 L1200 80Z" fill="#f7941d"/>
  <path d="M0 80 L0 62 Q400 45 700 62 Q950 72 1200 40 L1200 80Z" fill="#2b2b2b"/>
</svg>
<footer class="site-footer abs">
  <div class="brand abs">Brava Nest</div>
  <div class="foot-col abs" style="left:408px;top:46px">
    <h4>Quick Link</h4>
    <ul><li>Home</li><li>About Us</li><li>Areas Served</li><li>Pricing</li><li>Blog</li><li>Contact Us</li></ul>
  </div>
  <div class="foot-col abs" style="left:594px;top:46px">
    <h4>Contact Info</h4>
    <div class="info-row"><svg width="12" height="14" viewBox="0 0 12 14"><path d="M6 13C2 8 1 6 1 5a5 5 0 0110 0c0 1-1 3-5 8z" fill="none" stroke="#fff"/><circle cx="6" cy="5" r="1.8" fill="#fff"/></svg><span>48 Alder Lane, Westbrook,<br>New York 10000, USA</span></div>
    <div class="info-row" style="margin-top:40px"><svg width="12" height="12" viewBox="0 0 12 12"><rect x="1" y="2" width="10" height="8" fill="none" stroke="#fff"/></svg><span>00 555 010 4477</span></div>
    <div class="info-row" style="margin-top:6px"><svg width="12" height="12" viewBox="0 0 12 12"><rect x="1" y="2" width="10" height="8" fill="none" stroke="#fff"/><path d="M1 3l5 4 5-4" fill="none" stroke="#fff"/></svg><span>team@bravanest.example</span></div>
    <div class="info-row" style="margin-top:6px;color:var(--orange)"><svg width="12" height="12"><circle cx="6" cy="6" r="5" fill="none" stroke="#f7941d"/><path d="M3.5 6l2 2 3-3.5" fill="none" stroke="#f7941d"/></svg><span>Available 24/7 Hours a Day</span></div>
  </div>
  <div class="foot-col abs" style="left:867px;top:46px;width:255px">
    <h4>Quick Contact</h4>
    <div style="display:flex;gap:8px"><div class="field" style="width:124px">Name</div><div class="field" style="width:123px">Phone</div></div>
    <div class="field" style="height:60px;margin-top:6px">Message</div>
    <div class="btn btn--plain" style="width:255px;height:36px;margin-top:12px;border-radius:18px">Send</div>
  </div>
</footer>
<div class="copyright abs">Copyright © 2020 Brava Nest. All Right Reserved</div>
<div class="social abs" aria-label="Social links"><i class="first"></i><i></i><i></i><i></i></div>

</body>
</html>
```